ZELK LED WALL BUYERS GUIDE

We require a brcohure to send to our customers that sets out the provided text in a neat and clearly readable format, We wish to position this brochure as an information source that demonstrates us a market leader in this technology and not afraid to share what customers should be looking for in a new LED video wall. This will be used mostly in PDF format, will be multiple A4 pages and we are happy to include stock photos where required to further illustrate or show the technical nature of our business and products. Plenty of white space and easy to read is a MUST for this project. We have uploaded the text document and the logo we which to incorporate into this brochure.Brochure should include all our office address's (located at www.kemtrix.com.au)

Target Market(s)

Corporate, education, fitness, advertising, digital signage

Colors
0255a3
0455a3

Requirements
Must have
• Be easy to read, clean and tidy and be visually captivating.
• Promote our business as a knowlege based market leader
• Include the text we have already prepared
• Have our office addressed and contact numbers
• Include our corporate colours (www.kemtrix.com.au)
Nice to have
• Be easy to read
• Make potential customers "want to read it"
• We have the ZELK logo in AI and EPS format if needed

```html
<!DOCTYPE html>
<html lang="en">
<head>
<meta charset="utf-8">
<title>ZELK LED Video Wall Technology Guide</title>
<link href="https://fonts.googleapis.com/css2?family=Roboto:wght@300;400;500&family=PT+Sans:ital,wght@0,400;0,700;1,400;1,700&display=swap" rel="stylesheet">
<style>
:root{
  --stage:#6b6b6b;
  --paper:#ffffff;
  --brand:#0a0d8f;
  --ink:#222228;
  --muted:#77777d;
  --row:#e3e3e6;
}
*{box-sizing:border-box;margin:0;padding:0}
html,body{width:1200px;height:1200px;overflow:hidden;background:var(--stage)}
body{position:relative;font-family:"PT Sans",sans-serif;color:var(--ink)}
.page{position:absolute;width:394px;height:553px;background:var(--paper);box-shadow:4px 6px 12px rgba(0,0,0,.35);overflow:hidden}
.page--cover{left:167px;top:43px}
.page--intro{left:631px;top:43px}
.page--choose{left:379px;top:630px}
.abs{position:absolute}
.brand-mark{position:absolute;display:flex;align-items:center;gap:5px;font-family:"Roboto",sans-serif;color:var(--brand)}
.brand-mark i{display:block;background:currentColor}
.brand-mark--cover{right:16px;top:29px;font-size:12.5px;font-weight:400}
.brand-mark--cover i{width:14px;height:14px}
.brand-mark--foot{left:299px;top:524px;font-size:5px;color:var(--muted)}
.brand-mark--foot i{width:7px;height:7px}
.photo{position:absolute}
.cover-band{position:absolute;left:16px;top:410px;width:363px;height:98px;background:var(--brand);text-align:center;color:#fff;font-family:"Roboto",sans-serif}
.cover-title{font-weight:300;font-size:23px;line-height:27px;padding-top:8px;letter-spacing:.2px}
.cover-sub{position:absolute;left:29px;top:68px;width:306px;height:18px;background:#fff;color:var(--brand);font-size:12.5px;line-height:18px}
.cover-contact{position:absolute;left:0;right:0;top:524px;display:flex;justify-content:center;gap:18px;font-family:"Roboto",sans-serif;font-size:11px;font-weight:500;color:var(--ink)}
.cover-contact span{display:flex;align-items:center;gap:3px}
.marker{position:absolute;left:0;width:19px;background:var(--brand)}
.h1{position:absolute;font-family:"Roboto",sans-serif;color:var(--brand);font-weight:400}
.h-sub{font-family:"Roboto",sans-serif;color:var(--brand);font-weight:500}
.copy{font-size:6.6px;line-height:9.3px}
.copy p{margin-bottom:9.3px}
.copy em{font-style:italic;font-weight:700}
.item{position:absolute;left:123px;width:246px;display:flex;flex-direction:column}
.item .copy{font-size:6.4px;line-height:9px;letter-spacing:-.05px}
.item-title{font-family:"Roboto",sans-serif;color:var(--brand);font-size:8.5px;line-height:11px;font-weight:500}
.item-label{font-family:"Roboto",sans-serif;font-size:7.2px;line-height:11px;color:var(--ink)}
.item .gap{margin-bottom:4px}
.justify{text-align:justify}
.spec-table{position:absolute;left:31px;top:371px;width:343px;border-collapse:collapse;font-size:7.4px}
.spec-table th{background:var(--brand);color:#fff;font-family:"Roboto",sans-serif;font-weight:500;font-size:9px;height:21px;text-align:left;padding-left:12px}
.spec-table td{height:17px;padding-left:22px}
.spec-table tr.shade td{background:var(--row)}
</style>
</head>
<body>

<section class="page page--cover">
  <div class="brand-mark brand-mark--cover"><i></i>kemtrix media</div>

  <div class="photo" style="left:16px;top:70px;width:92px;height:162px;background:linear-gradient(160deg,#7a3b2a,#2d2a3a 55%,#4a5b2e)" role="img" aria-label="Silhouette of a person in front of a wall of video screens"></div>
  <div class="photo" style="left:114px;top:70px;width:130px;height:78px;background:linear-gradient(180deg,#2b2f3a,#3f7fae 50%,#c9ccd0)" role="img" aria-label="Ceiling mounted LED wall showing ocean footage in a lobby"></div>
  <div class="photo" style="left:249px;top:70px;width:130px;height:78px;background:linear-gradient(180deg,#8a9298,#2fb3c9 50%,#4a4f58)" role="img" aria-label="Technician installing a bright LED wall display"></div>
  <div class="photo" style="left:114px;top:154px;width:266px;height:78px;background:linear-gradient(180deg,#2e3448,#a4523b 45%,#1b1e28)" role="img" aria-label="Control room with a large curved video wall"></div>
  <div class="photo" style="left:16px;top:235px;width:118px;height:84px;background:linear-gradient(160deg,#b9bec4,#7c6a6a 50%,#4f5a3a)" role="img" aria-label="Building facade with an outdoor LED screen"></div>
  <div class="photo" style="left:138px;top:235px;width:118px;height:84px;background:linear-gradient(160deg,#3b2b2d,#b98a9a 50%,#231d22)" role="img" aria-label="Indoor LED wall in a dim venue"></div>
  <div class="photo" style="left:261px;top:235px;width:118px;height:84px;background:linear-gradient(180deg,#4a4a4c,#b1977a 55%,#4f3524)" role="img" aria-label="Reception area with an LED display behind the desk"></div>
  <div class="photo" style="left:16px;top:323px;width:240px;height:84px;background:linear-gradient(180deg,#3a3223,#2b7fd8 30%,#25aef0 70%,#2a2420)" role="img" aria-label="Large desktop computer screen shown on an LED wall"></div>
  <div class="photo" style="left:261px;top:323px;width:118px;height:84px;background:linear-gradient(180deg,#8ea6c0,#6b6f74 50%,#3c3f43)" role="img" aria-label="Street level advertising LED billboard"></div>

  <div class="cover-band">
    <div class="cover-title">ZELK LED VIDEO WALL<br>TECHNOLOGY GUIDE</div>
    <div class="cover-sub">WHAT YOU SHOULD CONSIDER?</div>
  </div>

  <div class="cover-contact">
    <span><svg width="8" height="8" viewBox="0 0 24 24"><path fill="currentColor" d="M6.6 10.8a15.1 15.1 0 0 0 6.6 6.6l2.2-2.2c.3-.3.7-.4 1-.2 1.1.4 2.3.6 3.6.6.6 0 1 .4 1 1V20c0 .6-.4 1-1 1A17 17 0 0 1 3 4c0-.6.4-1 1-1h3.5c.6 0 1 .4 1 1 0 1.3.2 2.5.6 3.6.1.3 0 .7-.2 1z"/></svg>1300 555 019</span>
    <span><svg width="9" height="7" viewBox="0 0 24 18"><path fill="currentColor" d="M0 0h24v18H0z"/><path fill="#fff" d="M1.5 1.5 12 10l10.5-8.5v1.8L12 11.8 1.5 3.3z"/></svg>info@kemtrix.com.au</span>
  </div>
</section>

<section class="page page--intro">
  <div class="marker" style="top:34px;height:15px"></div>
  <h1 class="h1" style="left:25px;top:29px;font-size:23px">Introduction</h1>
  <div class="abs copy" style="left:25px;top:58px;width:346px">
    <p><em>We have an incredible property, Ridgeline Business Park, located at 1180 Prairie Route 9, Harlow County, Easton Falls 50421 which we have fully funded with cash and now need a joint venture partner, buyer or lender to get this project to completion and producing a substantial profit we all can share.</em></p>
    <p><em>Our property is located on the best oil reserves in the region, with more oil than any other county in the basin and with the lowest recoverable costs of $24 a barrel.</em></p>
    <p><em>We own the property and need a partner to develop the site and bring to the market at half the cost of competing business parks in the area.</em></p>
    <p>LED display technology offers huge benefits in commercial applications due to the seamless and modular nature of the technology and its capability to operate in challenging environments.</p>
    <p>No other display technology on the market has the ability to provide impact and scale more so than an LED Video Wall. We believe it is essential that in order for the significant investment made in LED technology, to be deemed a complete success, we educate you (our customer) in the benefits and considerations when choosing this technology. We want you to be fully informed of your implementation process and your service journey.</p>
  </div>

  <div class="marker" style="top:264px;height:15px"></div>
  <h2 class="h1" style="left:25px;top:262px;font-size:14.5px">What Does An LED Display Solution Comprise Of?</h2>
  <div class="abs copy" style="left:26px;top:283px">In simple terms, a ZELK LED Video Wall solution consists of the following components:</div>

  <div class="photo" style="left:26px;top:299px;width:90px;height:58px;background:linear-gradient(90deg,#2a2f3a,#9aa3b5 50%,#2a2f3a)" role="img" aria-label="Rack of LED controller hardware"></div>
  <div class="item" style="top:300px">
    <div class="item-title">LED CONTROLLER</div>
    <div class="copy justify">The LED controller accepts a video signal from a source device such as a PC or scaling switch and transmits this video signal to each individual pixel on the LED display. Each LED video controller can manage a specific number of pixels and therefore it is common to have multiple LED controllers connected to a single LED display.</div>
  </div>

  <div class="photo" style="left:26px;top:370px;width:90px;height:59px;background:linear-gradient(100deg,#0d1b22,#1d8a3e 35%,#3454c8 65%,#0d1b22)" role="img" aria-label="Close-up of red, green and blue LED strips"></div>
  <div class="photo" style="left:26px;top:441px;width:90px;height:58px;background:linear-gradient(135deg,#f2c230,#e8e3cf 50%,#f2c230)" role="img" aria-label="Close-up of yellow surface mounted LED chips"></div>
  <div class="item" style="top:371px">
    <div class="item-title">LED TILE</div>
    <div class="item-label">LED panel</div>
    <div class="copy justify gap">The LED panel consists of a number of red, green and blue LED's mounted to a tile. The number of pixels on an LED panel varies significantly depending on pixel density and panel size. The video wall display is created by building a collection of LED panels.</div>
    <div class="item-label">Power supply</div>
    <div class="copy justify gap">A power supply is required for each LED panel that makes up the full LED display. This supply can be remotely located in a comms room or incorporated into the chassis of the LED panel. It is essential that the power supply is of excellent quality to ensure longevity.</div>
    <div class="item-label">Receiving card</div>
    <div class="copy">This unit receives the video signal from the video wall controller and sends it to each individual pixel on the LED panel.</div>
  </div>

  <div class="brand-mark brand-mark--foot"><i></i>kemtrix media</div>
</section>

<section class="page page--choose">
  <div class="marker" style="top:44px;height:14px"></div>
  <h2 class="h1" style="left:30px;top:41px;font-size:14.5px;line-height:18px">What Do I Need To Think About When Choosing<br>A ZELK LED Video Wall Display Solution?</h2>
  <div class="abs copy" style="left:31px;top:82px;width:340px">There are a number of requirements that need to be considered and discussed during project planning to ensure that the right LED Video Wall solution is successfully chosen and deployed:</div>

  <div class="abs h-sub" style="left:30px;top:124px;font-size:10px">CONTENT</div>
  <div class="abs copy" style="left:31px;top:142px;width:350px">
    <p>Understanding the required content is essential to any successful LED Video Wall installation. This is especially important when considering what shape or aspect ratio the LED display should be. Interesting shapes and sizes can provide exceptional impact, but will require further investment in specialised content production to remain engaging.</p>
    <p>Standard aspect ratios might not be as creative in physical design, but allow for simpler content creation.</p>
    <p style="margin-bottom:0">When running multiple content sources through a video wall controller, content layouts and pre-sets should be coordinated during the Video Wall design to ensure the required content can be delivered onto the Video Wall.<br>Ideally, sample content should be created and provided for testing, or during the LED selection criteria.</p>
  </div>

  <div class="abs h-sub" style="left:30px;top:266px;font-size:10px">SIZE</div>
  <div class="abs copy" style="left:31px;top:285px;width:350px">
    <p>Industry guidelines around the overall screen size apply for LED solutions, as they do for other display technologies.</p>
    <p>If an LED display is too small, it can be difficult to read detailed information. Too big, and it can be difficult to view all of the information in one single view.</p>
    <p>Taking into account minimum viewing distances for pixel pitch as detailed below, Kemtrix Media work to best practise standards when recommending the most appropriate display size for your application:</p>
  </div>

  <table class="spec-table">
    <tr><th style="width:118px">Level of Detail</th><th style="width:85px">Example</th><th>Viewers distance from display</th></tr>
    <tr class="shade"><td>Fine Detail</td><td style="padding-left:14px">Spreadsheet</td><td style="padding-left:28px">4 x Height of the Display</td></tr>
    <tr><td>General</td><td style="padding-left:14px">Presentation</td><td style="padding-left:28px">6 x Height of the Display</td></tr>
    <tr class="shade"><td>Video</td><td style="padding-left:14px">Video</td><td style="padding-left:28px">8 x Height of the Display</td></tr>
  </table>

  <div class="brand-mark brand-mark--foot"><i></i>kemtrix media</div>
</section>

</body>
</html>
```